Business Card for Industrial Distributor

We need a business card design for an industrial distributor. We sell machine parts for the manufacturing and oil industry. We would like the cards to look clean and modern but with a touch of industry.

Our colors are blue/white.

Please feel free to visit our website www.krovelmint.com

Target Market(s)

mexican manufacturers in the automobile/aerospace industry

Industry/Entity Type

Industrial

Colors
ffffff
0555a3

```html
<!DOCTYPE html>
<html lang="en">
<head>
<meta charset="utf-8">
<title>Krovelmint Business Card</title>
<link rel="stylesheet" href="https://fonts.googleapis.com/css2?family=Open+Sans:wght@300;400;600;700&display=swap">
<style>
  :root {
    --brand-blue: #0555a3;
    --brand-navy: #1f3a9a;
    --paper: #ffffff;
    --backdrop: #d6d6d6;
  }
  * { box-sizing: border-box; margin: 0; padding: 0; }
  html, body {
    width: 1200px;
    height: 800px;
    overflow: hidden;
    background: var(--backdrop);
    font-family: "Open Sans", Arial, sans-serif;
  }
  .sheet {
    width: 1200px;
    height: 800px;
    display: flex;
    align-items: center;
    justify-content: center;
    gap: 40px;
  }
  .card {
    position: relative;
    width: 540px;
    height: 309px;
    overflow: hidden;
    box-shadow: 0 2px 6px rgba(0,0,0,0.12);
  }
  /* Front */
  .card-front {
    background: var(--brand-blue);
    color: var(--paper);
  }
  .brand {
    display: flex;
    align-items: center;
    gap: 10px;
    font-weight: 700;
    letter-spacing: -0.5px;
  }
  .brand-dot {
    border-radius: 50%;
    background: currentColor;
    flex: none;
  }
  .card-front .brand {
    position: absolute;
    left: 50%;
    top: 118px;
    transform: translateX(-50%);
    font-size: 46px;
  }
  .card-front .brand-dot { width: 40px; height: 40px; }
  .front-web {
    position: absolute;
    left: 0; right: 0;
    bottom: 64px;
    text-align: center;
    font-size: 11px;
    letter-spacing: 0.4px;
  }
  /* Back */
  .card-back { background: var(--paper); }
  .back-panel {
    position: absolute;
    inset: 0;
    width: 100%;
    height: 100%;
  }
  .back-panel polygon { fill: var(--brand-blue); }
  .card-back .brand {
    position: absolute;
    left: 40px;
    top: 136px;
    font-size: 27px;
    color: var(--brand-navy);
  }
  .card-back .brand-dot { width: 24px; height: 24px; }
  .contact {
    position: absolute;
    right: 28px;
    top: 46px;
    text-align: right;
    color: var(--paper);
  }
  .contact-name {
    font-size: 26px;
    font-weight: 300;
    line-height: 1;
  }
  .contact-name strong { font-weight: 600; }
  .contact-role {
    font-size: 9px;
    letter-spacing: 4px;
    margin-top: 2px;
    margin-right: -4px;
  }
  .contact-lines {
    list-style: none;
    margin-top: 14px;
    font-size: 11.5px;
    line-height: 1.45;
  }
</style>
</head>
<body>
  <main class="sheet">
    <section class="card card-front" aria-label="Card front">
      <div class="brand"><span class="brand-dot"></span>Krovelmint</div>
      <p class="front-web">www.krovelmint.com</p>
    </section>

    <section class="card card-back" aria-label="Card back">
      <svg class="back-panel" viewBox="0 0 540 309" preserveAspectRatio="none" aria-hidden="true">
        <polygon points="328,0 540,0 540,309 255,309"/>
      </svg>
      <div class="brand"><span class="brand-dot"></span>Krovelmint</div>
      <div class="contact">
        <p class="contact-name">Marco <strong>Reyes</strong></p>
        <p class="contact-role">MANAGER</p>
        <ul class="contact-lines">
          <li>418 Harbor Road Lindale, MA</li>
          <li>377-410-628</li>
          <li>krovelmint@mail.com</li>
          <li>www.krovelmint.com</li>
        </ul>
      </div>
    </section>
  </main>
</body>
</html>
```